Eye-catching & Glamorous Labels for Skincare Bottles & Jars

We need new labels designed for our product range as we have been dormant for a few years and are now rebranding Tindra Mist - Cruelty Free Skincare. The label sizes are defined in the attached word document. All products have either a bright silver or a matte silver lid pump/spray so please keep this in mind.

We are open to colours and invite you to create bright trendy labels which are coordinated with the logo attached. The logo is not of any specific colour so dark on light, light on dark, tone on tone - we like purple / duck egg blue / turquoise WITH matte silver, however stronger colours like navy plus maroon with matte silver is also a strong favourite. If you feel inspired by a colour you think would be appropriate to Tindra Mist please feel free to have a go.

A front section for product information is required and the back should include relevant details ie ingredients, company info, and a note that there has been no testing on animals.

The serum bottle will require a front and back label on a clear label in a pale colour to coordinate with the rest of the range. Size for this label is 35mm top edge, 25mm bottom edge, height 45mm - I have attached a picture of the serum bottle as they were originally pad printed. Please don't hesitate to contact me for any further information. Good luck!

Target Market(s)

Educated professional women 30-45 who are regular skincare users and looking for beautiful skincare products without animal derived ingredients and animal testing

Industry/Entity Type

Skin Care Product

Font styles to use
Serif
Sans Serif
Decorative
Script

Colors

Designer to choose colors to be used in the design.

Requirements
Must have
• Tindra Mist Logo - eye catching design - not too busy or cramped.
Nice to have
• Is it possible to create a background pattern using a very small image of the logo? Just a thought.

```html
<!DOCTYPE html>
<html lang="en">
<head>
<meta charset="utf-8">
<title>Tindra Mist – Facial Scrub Jar Label</title>
<link rel="stylesheet" href="https://fonts.googleapis.com/css2?family=Questrial&family=Montserrat:wght@600&display=swap">
<style>
  :root {
    --page-bg: #e2e2e2;
    --teal-deep: #3e8587;
    --teal-mid: #4a9496;
    --teal-light: #d2f2f3;
    --ink: #1d2629;
  }
  * { margin: 0; padding: 0; box-sizing: border-box; }
  html, body {
    width: 1200px;
    height: 1200px;
    overflow: hidden;
    background: var(--page-bg);
  }
  .jar-label {
    position: absolute;
    left: 50px;
    top: 308px;
    width: 1100px;
    height: 584px;
    background: linear-gradient(90deg, var(--teal-deep) 0%, var(--teal-mid) 55%, #7fbcbe 80%, var(--teal-light) 100%);
  }
  .brand {
    position: absolute;
    left: 70px;
    top: 268px;
    width: 200px;
    display: flex;
    flex-direction: column;
    align-items: center;
    font-family: "Questrial", sans-serif;
    color: var(--ink);
    text-align: center;
  }
  .brand-mark {
    width: 54px;
    height: 54px;
    border: 3px solid var(--ink);
    border-radius: 50%;
    margin-bottom: 14px;
  }
  .brand-name {
    font-size: 30px;
    letter-spacing: 1px;
    line-height: 1.1;
  }
  .brand-tagline {
    font-size: 16px;
    letter-spacing: 0.5px;
    margin-top: 6px;
  }
  .product-frame {
    position: absolute;
    left: 310px;
    top: 250px;
    width: 728px;
    height: 150px;
    border: 3px solid var(--ink);
  }
  .product-frame::before {
    content: "";
    position: absolute;
    left: 8px;
    top: 60px;
    width: 4px;
    height: 56px;
    background: var(--ink);
  }
  .frame-rules {
    position: absolute;
    right: 14px;
    top: 20px;
    width: 80px;
  }
  .frame-rules span {
    display: block;
    height: 3px;
    background: var(--ink);
    margin-bottom: 8px;
  }
  .product-name {
    position: absolute;
    left: 26px;
    top: 38px;
    font-family: "Questrial", sans-serif;
    font-size: 82px;
    line-height: 1;
    letter-spacing: 2px;
    color: var(--ink);
  }
  .product-volume {
    position: absolute;
    right: 18px;
    bottom: 8px;
    font-family: "Questrial", sans-serif;
    font-size: 20px;
    color: var(--ink);
  }
  .product-claim {
    position: absolute;
    left: 318px;
    top: 418px;
    font-family: "Montserrat", sans-serif;
    font-weight: 600;
    font-size: 28px;
    letter-spacing: 1px;
    color: var(--ink);
  }
</style>
</head>
<body>
  <div class="jar-label">
    <div class="brand">
      <div class="brand-mark"></div>
      <div class="brand-name">Tindra Mist</div>
      <div class="brand-tagline">Cruelty Free Skincare</div>
    </div>

    <div class="product-frame">
      <div class="frame-rules">
        <span></span><span></span><span></span><span></span><span></span>
      </div>
      <h1 class="product-name">FACIAL SCRUB</h1>
      <div class="product-volume">30 ml</div>
    </div>

    <p class="product-claim">Anti Aging Arsenal</p>
  </div>
</body>
</html>
```